Business card (AI file uploaded)

We need a business card design that is minimalist using existing logo (attached). Source files must be editable so we can make the same design with other names.

Screenshots included of a design I was working on to give you an idea of the style I would like. Looking for similar modern styles

Thanks

```html
<!DOCTYPE html>
<html lang="en">
<head>
<meta charset="utf-8">
<title>Corvell Law Group — Business Card</title>
<link rel="stylesheet" href="https://fonts.googleapis.com/css2?family=Questrial&display=swap">
<style>
  :root {
    --stage-light: #ffffff;
    --stage-dark: #c9c9c9;
    --ink: #000000;
    --paper: #ffffff;
    --text-dark: #111111;
  }
  * { margin: 0; padding: 0; box-sizing: border-box; }
  html, body {
    width: 1034px;
    height: 1200px;
    overflow: hidden;
  }
  body {
    position: relative;
    background: radial-gradient(ellipse 62% 55% at 50% 50%, var(--stage-light) 40%, var(--stage-dark) 100%);
    font-family: "Questrial", "Century Gothic", sans-serif;
  }
  .card {
    position: absolute;
    left: 160px;
    width: 691px;
    height: 404px;
  }
  .card--front {
    top: 135px;
    background: var(--ink);
    color: var(--paper);
  }
  .card--back {
    top: 665px;
    background: var(--paper);
    color: var(--text-dark);
  }

  /* Front */
  .front-mark {
    position: absolute;
    left: 272px;
    top: 74px;
    width: 148px;
    height: 148px;
  }
  .firm-name {
    position: absolute;
    left: 0;
    right: 0;
    top: 240px;
    text-align: center;
    font-size: 48px;
    letter-spacing: 3px;
    line-height: 1;
    text-transform: uppercase;
  }
  .practice-areas {
    position: absolute;
    left: 0;
    right: 0;
    top: 362px;
    text-align: center;
    font-size: 19px;
    letter-spacing: 0.3px;
  }
  .practice-areas .divider { margin: 0 6px; }

  /* Back */
  .back-brand {
    position: absolute;
    left: 40px;
    top: 70px;
    width: 240px;
    text-align: center;
  }
  .back-brand svg { display: block; margin: 0 auto; }
  .back-brand__name {
    margin-top: 16px;
    font-size: 20px;
    letter-spacing: 2px;
    text-transform: uppercase;
    color: var(--ink);
  }
  .card-rule {
    position: absolute;
    left: 339px;
    top: 67px;
    width: 1.5px;
    height: 300px;
    background: var(--ink);
  }
  .person {
    position: absolute;
    right: 37px;
    top: 65px;
    text-align: right;
  }
  .person__name {
    font-size: 33px;
    letter-spacing: 1px;
    line-height: 1;
    text-transform: uppercase;
    font-weight: 400;
  }
  .person__title {
    margin-top: 4px;
    font-size: 18px;
  }
  .contact {
    position: absolute;
    right: 37px;
    top: 252px;
    text-align: right;
    font-size: 18px;
    line-height: 22.5px;
    font-style: normal;
  }
</style>
</head>
<body>
  <section class="card card--front">
    <svg class="front-mark" viewBox="0 0 148 148" aria-hidden="true">
      <circle cx="74" cy="74" r="70" fill="none" stroke="var(--paper)" stroke-width="6"/>
    </svg>
    <h1 class="firm-name">Corvell Law Group</h1>
    <p class="practice-areas">Real Estate<span class="divider">|</span>Bankruptcy<span class="divider">|</span>Social Security Disability</p>
  </section>

  <section class="card card--back">
    <div class="back-brand">
      <svg width="190" height="190" viewBox="0 0 190 190" aria-hidden="true">
        <circle cx="95" cy="95" r="92" fill="var(--ink)"/>
      </svg>
      <p class="back-brand__name">Corvell Law Group</p>
    </div>
    <div class="card-rule"></div>
    <div class="person">
      <h2 class="person__name">Jordan Corvell</h2>
      <p class="person__title">Attorney At Law</p>
    </div>
    <address class="contact">
      410 Meridian Ave., Suite 300<br>
      Lakeview, IL 60611<br>
      P: 630.555.0142<br>
      F: 630.555.0187<br>
      jordan@corvelllaw.com
    </address>
  </section>
</body>
</html>
```